Foot doctor needs feet friendly business cards.

Business cards for Podiatrist. Needs to look professional and modern. Back side put an appointment card, and try to put a little basic street map somewhere on card along with all of our contact info below:

Martin Posada, DPM, Inc.
Diplomate, National Council of Lower Limb Medicine
Call: 1.866.Toes.482
1.714.827.3391
Fax: 1.714.619.8042
Email: info@DrPosada.example
Web: www.DrPosada.example
2871 N. Willow Ave. Suite 204
Costa Mesa, CA 92626

```html
<!DOCTYPE html>
<html lang="en">
<head>
<meta charset="utf-8">
<title>Martin Posada, DPM, Inc. – Business Card</title>
<link rel="stylesheet" href="https://fonts.googleapis.com/css2?family=Carlito:wght@400;700&display=swap">
<style>
  :root {
    --backdrop: #6b6c6e;
    --card: #ffffff;
    --orange: #f58220;
    --ink: #231f20;
    --rule: #8a8a8a;
    --skin-light: #f8e2d3;
    --skin-mid: #efc4a8;
    --map-land: #ece7dc;
    --map-road: #f3c77a;
    --map-water: #c3d9ef;
  }
  * { box-sizing: border-box; margin: 0; padding: 0; }
  html, body {
    width: 1026px; height: 1200px; overflow: hidden;
    background: var(--backdrop);
    font-family: "Carlito", "Calibri", sans-serif;
    color: var(--ink);
  }
  .card {
    position: absolute; left: 32px; width: 962px;
    background: var(--card); overflow: hidden;
  }
  .card--front { top: 32px; height: 545px; }
  .card--back { top: 622px; height: 547px; }

  .front__photo {
    position: absolute; left: 0; top: 0; width: 540px; height: 545px;
    background: linear-gradient(115deg, rgba(255,255,255,0) 8%, var(--skin-light) 30%, var(--skin-mid) 55%, var(--skin-light) 78%, rgba(255,255,255,0) 96%);
  }
  .front__name {
    position: absolute; right: 41px; top: 38px;
    font-size: 38px; font-weight: 700; color: var(--orange); text-align: right; line-height: 1;
  }
  .front__credential {
    position: absolute; right: 41px; top: 86px;
    font-size: 25px; text-align: right; line-height: 1.2;
  }
  .front__band {
    position: absolute; left: 524px; top: 148px; width: 438px; height: 95px;
    background: var(--orange); color: #fff;
    font-size: 27px; font-weight: 700; line-height: 37px;
    text-align: right; padding: 9px 41px 0 0;
  }
  .front__contact {
    position: absolute; right: 41px; top: 278px; text-align: right;
  }
  .front__phone { font-size: 29px; line-height: 38px; }
  .front__web { font-size: 23px; line-height: 31px; }
  .front__web--first { margin-top: 3px; }
  .front__address {
    position: absolute; right: 41px; top: 472px; font-size: 23px; text-align: right;
  }

  .appointment__title {
    position: absolute; left: 0; width: 540px; top: 30px;
    font-size: 28px; font-weight: 700; text-align: center;
  }
  .appointment__field {
    position: absolute; left: 48px; width: 471px;
    display: flex; align-items: flex-end; font-size: 19px; height: 24px;
  }
  .appointment__field span { margin-right: 4px; line-height: 1; }
  .appointment__field i {
    flex: 1; border-bottom: 1px solid var(--rule); height: 1px; margin-bottom: 2px;
  }
  .appointment__map {
    position: absolute; left: 512px; top: 34px; width: 412px; height: 411px;
    background:
      radial-gradient(ellipse 80% 60% at 55% 20%, var(--map-road) 0%, rgba(243,199,122,0) 70%),
      linear-gradient(165deg, var(--map-land) 0%, var(--map-land) 35%, var(--map-water) 75%, var(--map-water) 100%);
  }
  .appointment__note {
    position: absolute; left: 48px; top: 478px; font-size: 19px; white-space: nowrap;
  }
</style>
</head>
<body>
  <section class="card card--front">
    <div class="front__photo" role="img" aria-label="Photo of a pair of bare feet"></div>
    <h1 class="front__name">Martin Posada, DPM, Inc.</h1>
    <p class="front__credential">Diplomate, National Council of Lower Limb Medicine</p>
    <div class="front__band">Nail Fungus laser Treatments<br>Heel Pain Relief Specialist</div>
    <div class="front__contact">
      <p class="front__phone">Call: 1-866-863-7482</p>
      <p class="front__phone">1-714-827-3391</p>
      <p class="front__phone">Fax: 1-714-619-8042</p>
      <p class="front__web front__web--first">Email: info@DrPosada.example</p>
      <p class="front__web">Web: www.DrPosada.example</p>
    </div>
    <p class="front__address">2871 N. Willow Ave., Suite 204, Costa Mesa, CA 92626</p>
  </section>

  <section class="card card--back">
    <h2 class="appointment__title">Appointment</h2>
    <div class="appointment__field" style="top:86px"><span>For:</span><i></i></div>
    <div class="appointment__field" style="top:153px"><span>Date:</span><i></i></div>
    <div class="appointment__field" style="top:220px"><span>Time:</span><i></i></div>
    <div class="appointment__field" style="top:286px"><span>Location:</span><i></i></div>
    <div class="appointment__field" style="top:352px"><i></i></div>
    <div class="appointment__field" style="top:418px"><i></i></div>
    <div class="appointment__map" role="img" aria-label="Street map of the coastal area with a pin marking the office location"></div>
    <p class="appointment__note">If you are unable to keep your appointment, Please&nbsp; contact us as soon as possible. Call 866-863-7482</p>
  </section>
</body>
</html>
```